Graphic design for Student Conference

We need design work done for our annual student conference called Willow Jamboree. We have a central logo but need design work done to use on posters, banners, etc. that tie into the theme for this year's conference. The theme is "Be Glad" and I would like the design elements to have a very fun, 1980's or 1990's vibe to them. The feeling of happiness and joy should be felt in the design.

Target Market(s)

Students 10-12 years of age

Industry/Entity Type

Church

Requirements
Must have
• Must include the Willow Jamboree logo - event date: June 19-21 - event website: brightcovechapel.org/willowjamboree - Flexible supporting artwork elements that can be used in a variety of mediums. - Must use fonts that are available from free, open sources or can be provided upon delivery of completed project.
Should not have
• Anything crude, scary or content inappropriate for middle school students. Should not have any imagery related to a classroom or meeting.

```html
<!DOCTYPE html>
<html lang="en">
<head>
<meta charset="utf-8">
<title>Willow Jamboree — June 19-21</title>
<link rel="stylesheet" href="https://fonts.googleapis.com/css2?family=Montserrat:wght@900&family=Gochi+Hand&display=swap">
<style>
  :root {
    --orange: #f89a05;
    --yellow: #f8d514;
    --paper: #ffffff;
    --purple: #8e009e;
    --pink: #f29fb3;
    --lilac: #d49ac6;
    --teal: #80d1c8;
    --blue: #0aa5bf;
    --coral: #fd6a4a;
    --white: #ffffff;
  }
  * { margin: 0; padding: 0; box-sizing: border-box; }
  html, body { width: 1200px; height: 1200px; overflow: hidden; background: var(--orange); }
  .poster { position: relative; width: 1200px; height: 1200px; overflow: hidden; }
  .poster-bands { position: absolute; inset: 0; }
  .logo {
    position: absolute; left: 0; top: 400px; width: 1200px;
    text-align: center; color: var(--purple);
    font-family: "Montserrat", sans-serif; font-weight: 900; line-height: 0.95;
  }
  .logo-line-1 { display: block; font-size: 150px; letter-spacing: -2px; }
  .logo-line-2 { display: block; font-size: 120px; letter-spacing: -1px; }
  .event-info {
    position: absolute; left: 605px; top: 1022px;
    color: var(--white); font-family: "Gochi Hand", cursive;
    transform: rotate(-14deg); transform-origin: left top;
    white-space: nowrap;
  }
  .event-date { font-size: 104px; line-height: 1; letter-spacing: 8px; margin-left: 28px; white-space: nowrap; }
  .event-url { font-size: 25px; line-height: 1.2; margin-top: 2px; white-space: nowrap; }
</style>
</head>
<body>
<main class="poster">
  <svg class="poster-bands" width="1200" height="1200" viewBox="0 0 1200 1200">
    <polygon fill="var(--paper)" points="0,248 1200,16 1200,872 0,1062"/>
    <polygon fill="var(--yellow)" points="0,268 1200,38 1200,852 0,1042"/>

    <g class="artwork">
      <circle role="img" aria-label="Smiling pink flower character" cx="120" cy="104" r="70" fill="var(--pink)"/>
      <circle role="img" aria-label="Smiling blue ball character" cx="269" cy="198" r="88" fill="var(--blue)"/>
      <circle role="img" aria-label="Smiling pink and yellow sun character" cx="1001" cy="127" r="130" fill="var(--lilac)"/>
      <circle role="img" aria-label="Large smiling pink flower character" cx="190" cy="989" r="165" fill="var(--pink)"/>
      <circle role="img" aria-label="Smiling coral ball character" cx="423" cy="1135" r="80" fill="var(--coral)"/>
      <circle role="img" aria-label="Smiling sun character peeking from the corner" cx="1140" cy="1180" r="90" fill="var(--lilac)"/>

      <rect role="img" aria-label="Teal squiggle decoration" x="380" y="270" width="260" height="60" rx="30" fill="var(--teal)" transform="rotate(-10 510 300)"/>
      <rect role="img" aria-label="Teal squiggle decoration" x="1030" y="240" width="170" height="60" rx="30" fill="var(--teal)" transform="rotate(-20 1115 270)"/>
      <rect role="img" aria-label="Teal squiggle decoration" x="0" y="600" width="120" height="55" rx="27" fill="var(--teal)" transform="rotate(-15 60 627)"/>
      <rect role="img" aria-label="Teal squiggle decoration" x="980" y="690" width="220" height="60" rx="30" fill="var(--teal)" transform="rotate(-18 1090 720)"/>
      <rect role="img" aria-label="Teal squiggle decoration" x="300" y="830" width="220" height="60" rx="30" fill="var(--teal)" transform="rotate(-25 410 860)"/>

      <circle role="img" aria-label="Lilac sparkle decoration" cx="744" cy="213" r="32" fill="var(--lilac)"/>
      <circle role="img" aria-label="Lilac sparkle decoration" cx="75" cy="780" r="28" fill="var(--lilac)"/>
      <circle role="img" aria-label="Lilac sparkle decoration" cx="856" cy="815" r="28" fill="var(--lilac)"/>

      <rect role="img" aria-label="Orange lightning bolt decoration" x="32" y="275" width="26" height="80" rx="6" fill="var(--orange)"/>
      <rect role="img" aria-label="Orange lightning bolt decoration" x="1150" y="370" width="26" height="80" rx="6" fill="var(--orange)"/>
      <rect role="img" aria-label="Orange lightning bolt decoration" x="650" y="740" width="28" height="90" rx="6" fill="var(--orange)"/>
    </g>
  </svg>

  <h1 class="logo">
    <span class="logo-line-1">Willow</span>
    <span class="logo-line-2">Jamboree</span>
  </h1>

  <div class="event-info">
    <p class="event-date">JUNE 19-21</p>
    <p class="event-url">www.brightcovechapel.org/willowjamboree</p>
  </div>
</main>
</body>
</html>
```